Rabbit Meat Label

We need a label for a shrink-wrapped tray of rabbit. The label does not need to be fancy, we just want a simple sticker to show customers a mock-up of what it may look like. The label is approximately 5" x 2.75". The label will go on top of the rabbit, so it will not lay flat. Please take that into consideration

The rabbit specifically is farm raised. Whole cut-up with 2 fore-legs, 2 hind legs and back.

There is nutritional information on the back, so please mention that somewhere on the label.

Industry/Entity Type

Farm

Requirements
Must have
• Please leave spaces for FQRB seals and other misc items. They are about 0.5" squares.
Should not have
• Do not have anything like "Made in the USA" or "All Natural." This will be added later, if need be.

```html
<!DOCTYPE html>
<html lang="en">
<head>
<meta charset="utf-8">
<title>Rabbit Meat Tray Label</title>
<link href="https://fonts.googleapis.com/css2?family=Lobster&family=Rye&family=Open+Sans:wght@700&display=swap" rel="stylesheet">
<style>
  :root {
    --paper: #ffffff;
    --brown: #6a3a1c;
    --badge-orange: #f4a640;
    --accent-orange: #e8643a;
    --ink: #141414;
    --band: #b9af99;
    --sky-wash: #c9dfee;
    --meadow-wash: #c6d8bd;
  }
  html, body {
    margin: 0;
    padding: 0;
    width: 1200px;
    height: 661px;
    overflow: hidden;
    background: var(--paper);
  }
  .label {
    display: block;
    width: 1200px;
    height: 661px;
  }
  .wash-sky { fill: none; stroke: var(--sky-wash); stroke-linecap: round; opacity: .75; }
  .wash-meadow { fill: none; stroke: var(--meadow-wash); stroke-linecap: round; opacity: .8; }
  .badge { fill: var(--badge-orange); }
  .badge-script {
    font-family: "Lobster", cursive;
    font-size: 32px;
    fill: var(--brown);
    stroke: var(--paper);
    stroke-width: 3px;
    paint-order: stroke;
  }
  .badge-sans {
    font-family: "Open Sans", sans-serif;
    font-weight: 700;
    font-size: 30px;
    fill: var(--ink);
  }
  .tray-note {
    font-family: "Rye", serif;
    font-size: 26px;
    fill: var(--accent-orange);
    letter-spacing: 1px;
  }
  .product-title {
    font-family: "Lobster", cursive;
    font-size: 150px;
    fill: var(--brown);
    stroke: var(--paper);
    stroke-width: 7px;
    paint-order: stroke;
    filter: drop-shadow(4px 6px 5px rgba(0,0,0,.45));
  }
  .connector {
    font-family: "Lobster", cursive;
    font-size: 26px;
    fill: var(--ink);
  }
  .cut-list {
    font-family: "Rye", serif;
    font-size: 32px;
    fill: var(--accent-orange);
  }
  .info-band { fill: var(--band); }
  .info-text {
    font-family: "Open Sans", sans-serif;
    font-weight: 700;
    font-size: 29px;
    fill: var(--ink);
  }
</style>
</head>
<body>
<svg class="label" viewBox="0 0 1200 661" xmlns="http://www.w3.org/2000/svg" aria-labelledby="label-title">
  <title id="label-title">Farm raised whole cut-up rabbit meat tray label</title>

  <g class="backdrop-washes">
    <path class="wash-sky" stroke-width="34" d="M230 190 C 380 150, 470 120, 620 110 S 900 150, 1190 120"/>
    <path class="wash-sky" stroke-width="28" d="M10 270 C 200 250, 380 200, 600 200 S 900 230, 1190 190"/>
    <path class="wash-sky" stroke-width="26" d="M20 340 C 250 320, 450 290, 700 290 S 1000 300, 1180 270"/>
    <path class="wash-meadow" stroke-width="30" d="M560 270 C 700 250, 880 250, 1180 250"/>
    <path class="wash-meadow" stroke-width="30" d="M20 440 C 250 420, 500 400, 700 390 S 1000 360, 1180 350"/>
  </g>

  <g class="badge-left" transform="translate(192 124) rotate(-22)">
    <ellipse class="badge" cx="0" cy="0" rx="142" ry="78"/>
    <text class="badge-script" x="-20" y="-12" text-anchor="middle">Farm Raised</text>
    <text class="badge-sans" x="22" y="26" text-anchor="middle">Whole cut-up</text>
  </g>

  <g class="badge-right" transform="translate(1020 124) rotate(28)">
    <ellipse class="badge" cx="0" cy="0" rx="142" ry="78"/>
    <text class="badge-script" x="-20" y="-12" text-anchor="middle">Farm Raised</text>
    <text class="badge-sans" x="18" y="26" text-anchor="middle">Whole cut-up</text>
  </g>

  <text class="tray-note" x="625" y="98" text-anchor="middle">FULL TRAY</text>

  <text class="product-title" x="612" y="385" text-anchor="middle" textLength="1020" lengthAdjust="spacingAndGlyphs" transform="rotate(-2 612 340)">Rabbit Meat</text>

  <text class="connector" x="652" y="455" text-anchor="middle">with</text>

  <text class="cut-list" x="604" y="540" text-anchor="middle" textLength="800" lengthAdjust="spacingAndGlyphs">2 FORE-LEGS, 2 HIND LEGS AND BACK.</text>

  <polygon class="info-band" points="0,581 1136,581 1194,621 1136,661 0,661"/>
  <text class="info-text" x="595" y="632" text-anchor="middle" textLength="920" lengthAdjust="spacingAndGlyphs">See back of package for all nutritional information.</text>
</svg>
</body>
</html>
```